Design an investor pitch deck for Brindlework.io

We delivered a killer investor pitch to a group of investors last week and have been asked for a deck. we need to follow up with a killer printed version. I have produced the attached file using free images from fotovane. Feel free to change the imagery as you see fit. Check out brindlework.io to get a feel for the look and feel we have right now.

Target Market(s)

Investors

Industry/Entity Type

Software

Font styles to use
Sans Serif
Other font styles liked:
• Helvetica

Requirements
Must have
• A new version of each of the pages in the example documents. Needs to be slick and professional
Nice to have
• Other layouts in case I add further slides
Should not have
• Childish or dated shapes or designs

```html
<!DOCTYPE html>
<html lang="en">
<head>
<meta charset="utf-8">
<title>Brindlework — Investor Deck</title>
<link rel="stylesheet" href="https://fonts.googleapis.com/css2?family=Arimo:wght@400;700&display=swap">
<style>
:root{
  --grey:#a9a9a9;
  --grey-light:#d9d9d9;
  --grey-text:#6b6b6b;
  --ink:#333;
  --navy:#2d4b8e;
  --navy-deep:#0c1a3a;
  --orange:#f5a623;
  --panel:#3b3b3b;
  --white:#fff;
}
*{box-sizing:border-box;margin:0;padding:0}
html,body{width:1200px;height:2180px;overflow:hidden;background:var(--white)}
body{font-family:"Arimo",Helvetica,Arial,sans-serif;color:var(--ink);position:relative}
.slide{position:absolute;overflow:hidden;background:var(--white)}
.photo{position:absolute}
.photo-network{background:radial-gradient(ellipse at 60% 70%,#3d6fb8 0%,#1a3266 35%,var(--navy-deep) 75%)}
.header{position:absolute;left:0;top:0;height:40px;width:100%;background:var(--grey);color:var(--white);font-size:21px;display:flex;align-items:center;justify-content:center}
.mark{position:absolute;width:28px;height:28px;border-radius:50%;background:var(--white)}
.header .mark{left:8px;top:6px}
.brand{font-weight:700;color:var(--white)}
.name-card{position:absolute;font-size:10px;line-height:1.35;text-align:right;color:var(--grey-text)}
.tiny{font-size:8.5px;line-height:1.3;color:var(--grey-text)}
.icon{position:absolute;width:26px;height:26px;border-radius:50%;border:1.5px solid var(--grey);}
.ticks{list-style:none;font-size:14px;line-height:1.3;color:var(--ink)}
.ticks li{position:relative;padding-left:22px;margin-bottom:16px}
.ticks li::before{content:"";position:absolute;left:3px;top:3px;width:5px;height:9px;border:solid var(--grey);border-width:0 2px 2px 0;transform:rotate(45deg)}
.pill{position:absolute;height:26px;background:var(--grey);color:var(--white);font-size:13px;display:flex;align-items:center;padding-left:14px}
.partner{font-size:12px;font-weight:700;color:var(--ink)}
</style>
</head>
<body>

<!-- Row 1 -->
<div class="photo" style="left:0;top:0;width:268px;height:290px;background:linear-gradient(135deg,#cfc8c0,#6e6761 55%,#2d2a28)" role="img" aria-label="Close-up of a hand checking a wristwatch"></div>

<section class="slide title-light" style="left:277px;top:0;width:249px;height:290px">
  <span class="mark" style="left:20px;top:78px;background:var(--grey)"></span>
  <h1 style="position:absolute;left:20px;top:108px;font-size:30px;color:var(--navy);font-weight:700">Brindlework</h1>
  <p style="position:absolute;left:20px;top:146px;font-size:15px;color:var(--grey-text);line-height:1.2">Waiting sucks. Brindlework<br>makes it better</p>
  <div class="name-card" style="right:10px;top:214px">Marcus Hale<br>Founder &amp; Head of Engineering<br>marcus@brindlework.io</div>
</section>

<section class="slide title-dark" style="left:530px;top:0;width:522px;height:290px">
  <div class="photo photo-network" style="inset:0" role="img" aria-label="Network of connected delivery icons over a city at night"></div>
  <div style="position:absolute;left:0;top:0;width:520px;height:108px;background:rgba(169,169,169,.92)"></div>
  <span class="mark" style="left:10px;top:14px"></span>
  <div class="brand" style="position:absolute;left:50px;top:10px;font-size:30px">Brindlework</div>
  <div style="position:absolute;left:50px;top:52px;font-size:17px;color:var(--white);line-height:1.15">Waiting sucks. Brindlework makes it<br>better.</div>
  <div class="name-card" style="right:6px;bottom:8px;background:rgba(255,255,255,.85);padding:6px 8px;color:var(--ink)">Marcus Hale<br>Founder &amp; Head of Engineering<br>marcus@brindlework.io</div>
</section>

<!-- Row 2 -->
<section class="slide title-band" style="left:9px;top:315px;width:517px;height:290px">
  <div class="photo photo-network" style="inset:0" role="img" aria-label="Network of connected delivery icons over a city at night"></div>
  <div style="position:absolute;left:0;top:0;width:517px;height:98px;background:rgba(169,169,169,.92)"></div>
  <span class="mark" style="left:8px;top:10px"></span>
  <div class="brand" style="position:absolute;left:50px;top:8px;font-size:30px">Brindlework</div>
  <div style="position:absolute;left:50px;top:50px;font-size:17px;color:var(--white);line-height:1.15">Waiting sucks. Brindlework makes it<br>better.</div>
  <div style="position:absolute;left:0;bottom:0;width:100%;height:32px;background:var(--navy)"></div>
  <div class="name-card" style="right:6px;bottom:10px;background:var(--white);padding:6px 8px;color:var(--ink)">Marcus Hale<br>Founder &amp; Head of Engineering<br>marcus@brindlework.io</div>
</section>

<section class="slide title-split" style="left:539px;top:315px;width:513px;height:290px">
  <div class="photo photo-network" style="left:0;top:0;width:513px;height:150px" role="img" aria-label="Network of connected delivery icons over a city at night"></div>
  <span class="mark" style="left:30px;top:170px;width:40px;height:40px;background:var(--grey)"></span>
  <div class="name-card" style="left:10px;top:228px;text-align:left">Marcus Hale<br>Founder &amp; Head of Engineering<br>marcus@brindlework.io</div>
  <div style="position:absolute;left:156px;top:145px;width:357px;height:145px;background:var(--navy)"></div>
  <div class="brand" style="position:absolute;left:176px;top:183px;font-size:29px">Brindlework</div>
  <div style="position:absolute;left:176px;top:222px;font-size:15px;color:var(--white)">Waiting Sucks. Brindlework Makes It Better.</div>
</section>

<!-- Row 3 -->
<section class="slide big-idea" style="left:0;top:628px;width:526px;height:306px">
  <div class="header"><span class="mark"></span>The Big Idea in 125 words</div>
  <p style="position:absolute;left:20px;top:52px;width:486px;text-align:center;font-size:18px;line-height:1.35;color:var(--ink)">Waiting sucks. Live tracking makes waiting for deliveries and services less painful. Brindlework makes it easy.</p>
  <span class="icon" style="left:60px;top:112px"></span>
  <span class="icon" style="left:230px;top:112px"></span>
  <span class="icon" style="left:400px;top:112px"></span>
  <p class="tiny" style="position:absolute;left:10px;top:148px;width:150px">People still wait at home for deliveries and services. Without live tracking, businesses lose time and customers lose patience and trust.</p>
  <p class="tiny" style="position:absolute;left:185px;top:148px;width:150px">Why haven't businesses used live tracking before? Legacy processes, complex systems and multiple providers left a gap no easy solution filled.</p>
  <p class="tiny" style="position:absolute;left:360px;top:148px;width:155px">Brindlework is the easiest way to give customers a live view of their delivery, helping businesses cut calls, missed jobs and empty waiting time.</p>
</section>

<section class="slide why-now" style="left:541px;top:628px;width:526px;height:306px">
  <div class="header"><span class="mark"></span>Why Now?</div>
  <svg style="position:absolute;left:0;top:50px" width="526" height="130" aria-hidden="true">
    <g fill="none" stroke="#a9a9a9" stroke-width="1.5">
      <circle cx="90" cy="60" r="55"/><circle cx="230" cy="60" r="55"/><circle cx="370" cy="60" r="55"/>
    </g>
    <path d="M145 60 l8 -6 v12z M285 60 l8 -6 v12z" fill="#a9a9a9"/>
  </svg>
  <div style="position:absolute;left:40px;top:88px;width:100px;text-align:center;font-size:14px;color:var(--grey-text)">Simple Global Deployment</div>
  <div style="position:absolute;left:180px;top:88px;width:100px;text-align:center;font-size:14px;color:var(--grey-text)">Success of best in class integrator</div>
  <div style="position:absolute;left:320px;top:88px;width:100px;text-align:center;font-size:14px;color:var(--grey-text)">Shifting Customer Expectation</div>
  <div class="partner" style="position:absolute;left:50px;top:196px;line-height:1.6">Boxanto<br>Crustway</div>
  <div class="partner" style="position:absolute;left:190px;top:196px;line-height:1.6">Tillquay<br>Cloudmere · Huddlewick</div>
  <div class="partner" style="position:absolute;left:340px;top:196px;line-height:1.6">Boxanto · Crustway<br>Rideaway · Rovenna</div>
</section>

<!-- Row 4 -->
<section class="slide solution" style="left:0;top:947px;width:526px;height:290px">
  <div class="header"><span class="mark"></span>The Solution</div>
  <span class="icon" style="left:60px;top:120px"></span>
  <span class="icon" style="left:200px;top:120px"></span>
  <span class="icon" style="left:335px;top:65px"></span>
  <span class="icon" style="left:335px;top:150px"></span>
  <svg style="position:absolute;left:0;top:0" width="526" height="290" aria-hidden="true">
    <g stroke="#a9a9a9" stroke-width="1.2" fill="none">
      <path d="M100 133 H190"/><path d="M235 128 L325 80"/><path d="M235 138 L325 163"/>
    </g>
  </svg>
  <p class="tiny" style="position:absolute;left:25px;top:155px;width:100px;text-align:center">Integration with common sources of jobs and automation to fit the device</p>
  <p class="tiny" style="position:absolute;left:165px;top:155px;width:100px;text-align:center">Simple endpoint for keeping things in a fast and simple workflow</p>
  <p class="tiny" style="position:absolute;left:370px;top:66px;width:140px">A clean, intuitive driver app which allows drivers to track jobs</p>
  <p class="tiny" style="position:absolute;left:370px;top:152px;width:140px">A customer-facing live service SMS and updates with links</p>
</section>

<section class="slide market-size" style="left:541px;top:947px;width:526px;height:290px">
  <div class="header"><span class="mark"></span>Market Size</div>
  <ol class="tiny" style="position:absolute;left:10px;top:62px;width:175px;list-style:none">
    <li style="margin-bottom:22px">1&nbsp;&nbsp; 1.35 billion annual deliveries in Australia by 2021</li>
    <li style="margin-bottom:22px">2&nbsp;&nbsp; Global e-commerce deliveries expected to reach 4 billion</li>
    <li>3&nbsp;&nbsp; Based on our bottom-up estimate a 3% share of the market will be US$23m in 2018</li>
  </ol>
  <svg style="position:absolute;left:195px;top:52px" width="320" height="220" aria-label="Stacked bar chart of delivery volume by region">
    <line x1="10" y1="185" x2="310" y2="185" stroke="#bbb"/>
    <g>
      <rect x="18" y="10" width="16" height="175" fill="#9a9a9a"/><rect x="18" y="70" width="16" height="115" fill="var(--orange)"/>
      <rect x="44" y="20" width="16" height="165" fill="#9a9a9a"/><rect x="44" y="80" width="16" height="105" fill="var(--orange)"/>
      <rect x="70" y="35" width="16" height="150" fill="#9a9a9a"/><rect x="70" y="90" width="16" height="95" fill="var(--orange)"/>
      <rect x="96" y="45" width="16" height="140" fill="#9a9a9a"/><rect x="96" y="100" width="16" height="85" fill="var(--orange)"/>
      <rect x="122" y="60" width="16" height="125" fill="#9a9a9a"/><rect x="122" y="110" width="16" height="75" fill="var(--orange)"/>
      <rect x="148" y="95" width="16" height="90" fill="#9a9a9a"/><rect x="148" y="125" width="16" height="60" fill="var(--orange)"/>
      <rect x="174" y="130" width="16" height="55" fill="#9a9a9a"/><rect x="174" y="150" width="16" height="35" fill="var(--orange)"/>
      <rect x="200" y="150" width="16" height="35" fill="#9a9a9a"/><rect x="200" y="162" width="16" height="23" fill="var(--orange)"/>
      <rect x="226" y="158" width="16" height="27" fill="#9a9a9a"/><rect x="226" y="168" width="16" height="17" fill="var(--orange)"/>
      <rect x="252" y="162" width="16" height="23" fill="#9a9a9a"/><rect x="252" y="171" width="16" height="14" fill="var(--orange)"/>
      <rect x="278" y="166" width="16" height="19" fill="#9a9a9a"/><rect x="278" y="174" width="16" height="11" fill="var(--orange)"/>
    </g>
  </svg>
</section>

<!-- Row 5 -->
<section class="slide business-model" style="left:0;top:1242px;width:526px;height:224px">
  <div class="header" style="width:493px"><span class="mark"></span>Business Model</div>
  <span class="icon" style="left:4px;top:66px;width:20px;height:20px"></span>
  <div class="pill" style="left:40px;top:63px;width:225px">Transactional pricing</div>
  <span class="icon" style="left:4px;top:109px;width:20px;height:20px"></span>
  <div class="pill" style="left:40px;top:106px;width:270px">Brindlework 15c per task (USD)</div>
  <span class="icon" style="left:4px;top:152px;width:20px;height:20px"></span>
  <div class="pill" style="left:55px;top:149px;width:330px">Credit and top up like a pre-paid phone card</div>
  <span class="icon" style="left:4px;top:189px;width:20px;height:20px"></span>
  <div class="pill" style="left:55px;top:186px;width:345px">Bonus credit for higher top up amounts</div>
</section>

<section class="slide go-to-market" style="left:526px;top:1242px;width:526px;height:224px">
  <div class="header" style="left:10px;width:516px"><span class="mark"></span>Go To Market</div>
  <p class="tiny" style="position:absolute;left:16px;top:46px;width:500px">Brindlework has a simple plan to grow: work with local businesses to prove the model, then partner with integrators who bring many customers at once.</p>
  <svg style="position:absolute;left:0;top:70px" width="220" height="154" aria-hidden="true">
    <circle cx="120" cy="78" r="74" fill="var(--orange)"/>
    <circle cx="112" cy="80" r="58" fill="#fff"/>
    <circle cx="112" cy="80" r="50" fill="var(--orange)"/>
    <circle cx="106" cy="82" r="38" fill="#fff"/>
    <circle cx="106" cy="82" r="32" fill="#bdbdbd"/>
  </svg>
  <p class="tiny" style="position:absolute;left:6px;top:112px;width:66px;background:var(--white);color:var(--ink)">Our go-to market plan is building a repeatable sales process</p>
  <p class="tiny" style="position:absolute;left:225px;top:88px;width:290px">Connect with business owners through integrators and trade networks that already reach our target users.</p>
  <p class="tiny" style="position:absolute;left:225px;top:128px;width:290px">Lead with a clear trial and onboarding plan so every account grows over time.</p>
  <p class="tiny" style="position:absolute;left:225px;top:172px;width:290px">Support each client closely and turn results into case studies.</p>
</section>

<!-- Row 6 -->
<section class="slide team" style="left:0;top:1480px;width:536px;height:352px">
  <div style="position:absolute;left:0;top:0;width:185px;height:352px;background:var(--panel)"></div>
  <span class="mark" style="left:20px;top:110px;width:60px;height:60px"></span>
  <div style="position:absolute;left:16px;top:200px;font-size:22px;color:var(--white)">Our Team</div>
  <ul class="ticks" style="position:absolute;left:200px;top:60px;width:320px">
    <li>Unique access to technical talent pipeline from our partnership with and colocation at Kestrel Vale Institute</li>
    <li>Battle hardened from bootstrapping for 3 years</li>
    <li>All key players have skin in the game</li>
    <li>Founder &amp; board's commercial experience</li>
  </ul>
</section>

<section class="slide finance" style="left:541px;top:1530px;width:526px;height:180px">
  <div class="header" style="width:520px"><span class="mark"></span>Finance &amp; Opportunity</div>
  <div style="position:absolute;left:40px;top:84px;font-size:13px;color:var(--grey-text)">2016</div>
  <div style="position:absolute;left:243px;top:84px;font-size:13px;color:var(--grey-text)">Now</div>
  <div style="position:absolute;left:400px;top:84px;font-size:13px;color:var(--grey-text)">6-9 months</div>
  <svg style="position:absolute;left:0;top:120px" width="526" height="40" aria-hidden="true">
    <polygon points="40,6 140,6 146,14 140,22 40,22" fill="#3b3b3b"/>
    <line x1="150" y1="14" x2="210" y2="14" stroke="var(--orange)" stroke-width="1.5" stroke-dasharray="3 3"/>
    <polygon points="215,6 300,6 306,14 300,22 215,22" fill="#3b3b3b"/>
    <line x1="310" y1="14" x2="375" y2="14" stroke="var(--orange)" stroke-width="1.5" stroke-dasharray="3 3"/>
    <polygon points="380,6 470,6 476,14 470,22 380,22" fill="#3b3b3b"/>
  </svg>
  <div style="position:absolute;left:40px;top:150px;font-size:12px;color:var(--orange)">$250k FFF</div>
  <div style="position:absolute;left:230px;top:150px;font-size:12px;color:var(--orange)">Deal details</div>
  <div style="position:absolute;left:392px;top:150px;font-size:12px;color:var(--orange)">Planned raise</div>
</section>

<!-- Row 7 -->
<section class="slide fuel-growth" style="left:9px;top:1838px;width:517px;height:307px">
  <div class="header"><span class="mark"></span>How to Fuel Growth</div>
  <svg style="position:absolute;left:0;top:0" width="517" height="307" aria-hidden="true">
    <g fill="none" stroke="#a9a9a9" stroke-width="1.2">
      <rect x="155" y="95" width="46" height="36" rx="6"/><rect x="310" y="95" width="46" height="36" rx="6"/>
      <rect x="155" y="180" width="46" height="36" rx="6"/><rect x="310" y="180" width="46" height="36" rx="6"/>
    </g>
    <circle cx="255" cy="155" r="48" fill="#555"/>
    <circle cx="255" cy="155" r="18" fill="#fff"/>
  </svg>
  <div style="position:absolute;left:40px;top:98px;width:100px;text-align:right;font-size:13px">Digital marketing expertise</div>
  <div style="position:absolute;left:40px;top:186px;width:100px;text-align:right;font-size:13px">AI-tailored digital campaign</div>
  <div style="position:absolute;left:375px;top:106px;width:130px;font-size:13px">Ramp up UK efforts</div>
  <div style="position:absolute;left:375px;top:186px;width:130px;font-size:13px">Customer journey management</div>
</section>

<section class="slide summary" style="left:560px;top:1838px;width:530px;height:307px;border-top:1px solid #999">
  <div class="photo" style="left:0;top:12px;width:140px;height:295px;background:radial-gradient(circle at 70% 55%,#e7cfa7,#b58a57 45%,#5a4230)" role="img" aria-label="Close-up of a desk globe"></div>
  <h2 style="position:absolute;left:170px;top:30px;font-size:22px;font-weight:400;color:var(--ink)">Summary</h2>
  <ul class="ticks" style="position:absolute;left:176px;top:80px;width:310px;font-size:12.5px">
    <li style="margin-bottom:12px">A clear problem for a big market</li>
    <li style="margin-bottom:12px">The right people and a great pipeline of talent</li>
    <li style="margin-bottom:12px">Great technology foundation and technical skills</li>
    <li style="margin-bottom:12px">Paying customers in multiple countries</li>
    <li style="margin-bottom:12px">A clear opportunity for capital to create and drive high growth engine</li>
  </ul>
  <span class="mark" style="left:500px;top:275px;width:18px;height:18px;background:var(--navy)"></span>
</section>

</body>
</html>
```